Meridian Sound Wellness LLC Card Design

Need business card with a logo for a hearing aid sales and audiology business. We have two Hearing Instrument Specialists and one Audiologist on staff. Over 25 years in business. Locally owned and operated. Financing available. Most insurances accepted.

Meridian Sound Wellness LLC
48730 W Linden Row, Suite 9
Spokane, WA 99481
509-617-2085
www.meridiansoundnorth.example

Manager
Tobias Wrenfield HIS COHC
License #81729046

Target Market(s)

50yr old + people with a hearing loss.

Industry/Entity Type

Business

Contact Information for Business Card

48730 W Linden Row, Suite 9
Spokane, WA 99481
509-617-2085
www.meridiansoundnorth.example

Manager
Tobias Wrenfield HIS COHC
NRPL #81729046

Font styles to use
Serif
Sans Serif

Requirements
Must have
• Business name, Tobias's name and title(s) and contact information, License #, web address
Nice to have
Should not have

```html
<!DOCTYPE html>
<html lang="en">
<head>
<meta charset="utf-8">
<title>Meridian Sound Wellness LLC – Business Card</title>
<link rel="stylesheet" href="https://fonts.googleapis.com/css2?family=Jost:wght@300;400;700&family=Advent+Pro:wght@400;500&display=swap">
<style>
  :root {
    --backdrop: #e4e7ea;
    --green-light: #33b24a;
    --green-band: #179f48;
    --white: #ffffff;
    --rule: rgba(255,255,255,0.45);
  }
  * { margin: 0; padding: 0; box-sizing: border-box; }
  html, body {
    width: 1200px; height: 746px; overflow: hidden;
    background: var(--backdrop);
  }
  .canvas {
    position: relative; width: 1200px; height: 746px;
    display: flex; align-items: center; justify-content: center;
  }
  .card {
    position: relative; width: 1050px; height: 600px;
    background: var(--green-light);
    color: var(--white);
    font-family: 'Jost', sans-serif;
    box-shadow: 0 10px 30px rgba(0,0,0,0.18);
    overflow: hidden;
  }
  .brand {
    position: absolute; left: 48px; top: 40px;
    display: flex; align-items: center; gap: 14px;
  }
  .brand-dot {
    width: 34px; height: 34px; border-radius: 50%;
    border: 3px solid var(--white);
  }
  .brand-name {
    font-weight: 300; font-size: 24px; letter-spacing: 0.5px;
  }
  .band {
    position: absolute; left: 0; right: 0; top: 115px; height: 345px;
    background: var(--green-band);
    box-shadow: 0 4px 8px rgba(0,0,0,0.18), 0 -4px 8px rgba(0,0,0,0.12);
  }
  .person {
    position: absolute; left: 48px; top: 42px; width: 540px;
  }
  .person-first {
    font-weight: 700; font-size: 92px; line-height: 0.95;
  }
  .person-last {
    font-weight: 300; font-size: 56px; line-height: 1.15; white-space: nowrap;
  }
  .person-role, .person-license {
    font-weight: 400; font-size: 32px; line-height: 1.25; margin-left: 44px;
  }
  .person-license { margin-left: 64px; }
  .contact {
    position: absolute; right: 48px; top: 34px; width: 392px;
    list-style: none;
  }
  .contact-item {
    display: flex; align-items: center; gap: 20px;
    padding: 20px 0;
    border-bottom: 1px solid var(--rule);
    font-size: 21px; font-weight: 400; line-height: 1.25;
  }
  .contact-item:last-child { border-bottom: none; }
  .contact-icon { width: 30px; height: 30px; flex: none; }
  .company {
    position: absolute; left: 0; right: 0; bottom: 48px;
    text-align: center;
    font-family: 'Advent Pro', sans-serif; font-weight: 500;
    font-size: 54px; letter-spacing: 3px;
  }
</style>
</head>
<body>
<div class="canvas">
  <article class="card">
    <div class="brand">
      <span class="brand-dot"></span>
      <span class="brand-name">Meridian Sound Wellness</span>
    </div>

    <section class="band">
      <div class="person">
        <div class="person-first">Tobias</div>
        <div class="person-last">Wrenfield HIS COHC</div>
        <div class="person-role">Manager</div>
        <div class="person-license">License #81729046</div>
      </div>

      <ul class="contact">
        <li class="contact-item">
          <svg class="contact-icon" viewBox="0 0 30 30" aria-hidden="true">
            <path d="M3 10c0-4 6-6 12-6s12 2 12 6v2h-6v-3H9v3H3z" fill="#fff"/>
            <rect x="6" y="14" width="18" height="12" rx="2" fill="#fff"/>
            <circle cx="15" cy="20" r="3" fill="#179f48"/>
          </svg>
          <span>509-617-2085</span>
        </li>
        <li class="contact-item">
          <svg class="contact-icon" viewBox="0 0 30 30" aria-hidden="true" fill="none" stroke="#fff" stroke-width="2">
            <circle cx="15" cy="15" r="12"/>
            <ellipse cx="15" cy="15" rx="5" ry="12"/>
            <line x1="3" y1="15" x2="27" y2="15"/>
            <line x1="5" y1="9" x2="25" y2="9"/>
            <line x1="5" y1="21" x2="25" y2="21"/>
          </svg>
          <span>www.meridiansoundnorth.example</span>
        </li>
        <li class="contact-item">
          <svg class="contact-icon" viewBox="0 0 30 30" aria-hidden="true">
            <path d="M15 2a9 9 0 0 0-9 9c0 7 9 17 9 17s9-10 9-17a9 9 0 0 0-9-9z" fill="#fff"/>
            <circle cx="15" cy="11" r="3.5" fill="#179f48"/>
          </svg>
          <span>48730 W Linden Row, Suite 9<br>Spokane, WA 99481</span>
        </li>
      </ul>
    </section>

    <div class="company">Meridian Sound Wellness LLC</div>
  </article>
</div>
</body>
</html>
```